依頼詳細
全体の基本としては、黒色を希望しますが、良い案があればお任せしたいと思います。
弊社のブランドロゴ(添付画像のB-5のデザイン)MELVOTAをさりげなくつけてください。
今までのパッケージのデザインも参考までに添付しておきます。
記載項目
蓋のサイズ210×60×18(添付画像参照)です。
底のサイズ205×55×35、底の部分は、黒色等の無地でもOKです。
希望イメージ
シンプル 複雑
単色 カラフル
暗い 明るい
日常 高級
遊び心 厳粛
未来的 伝統的
女性的 男性的
希望する色
全体としては黒色ですが、カラフル華やかに
納品ファイル
• イラストレーター形式 (.ai)
補足説明
繊細で透明感があり、カラフルな感じにしてもらえたらと思います。「GLASS PEN」と文字、またはグラスペンの形をデザインしたものが蓋の部分にあると嬉しいです。

色のバランス、インパクトです。

多くのご提案ありがとうございます。

```html
<!DOCTYPE html>
<html lang="en">
<head>
<meta charset="utf-8">
<title>MELVOTA Glass Pen Packaging</title>
<link rel="stylesheet" href="https://fonts.googleapis.com/css2?family=Marcellus&display=swap">
<style>
  :root {
    --canvas-bg: #ffffff;
    --ink-black: #0b0b0c;
    --ink-brown: #2a211c;
    --label-grey: #2e2c2d;
    --name-white: #f4f2ee;
    --accent-orange: #e8a13a;
    --accent-pink: #e0407a;
    --accent-blue: #4aa8d8;
    --strand-cyan: rgba(60, 200, 220, 0.55);
    --strand-magenta: rgba(230, 70, 150, 0.5);
    --strand-yellow: rgba(240, 220, 60, 0.5);
    --strand-green: rgba(110, 220, 90, 0.45);
    --strand-violet: rgba(150, 110, 240, 0.5);
    --type-serif: "Marcellus", serif;
  }

  * { box-sizing: border-box; margin: 0; padding: 0; }

  html, body {
    width: 1200px;
    height: 640px;
    overflow: hidden;
    background: var(--canvas-bg);
  }

  .sheet {
    position: relative;
    width: 1200px;
    height: 640px;
    font-family: var(--type-serif);
  }

  .sleeve {
    position: absolute;
    top: 136px;
    height: 390px;
    overflow: hidden;
    background: var(--ink-black);
  }
  .sleeve--front { left: 44px;  width: 136px; }
  .sleeve--side  { left: 186px; width: 128px; }
  .sleeve--back  { left: 324px; width: 126px; background: var(--ink-brown); }

  .strand-field {
    position: absolute;
    inset: 0;
    background:
      linear-gradient(90deg,
        var(--strand-cyan) 0%, transparent 12%,
        var(--strand-magenta) 22%, transparent 34%,
        var(--strand-yellow) 46%, transparent 56%,
        var(--strand-green) 66%, transparent 78%,
        var(--strand-violet) 88%, transparent 100%),
      var(--ink-black);
  }

  .fountain-field {
    position: absolute;
    left: 0; right: 0; top: 0;
    height: 250px;
    background:
      radial-gradient(ellipse 70% 90% at 50% 0%,
        rgba(120, 180, 230, 0.45) 0%,
        rgba(230, 90, 150, 0.3) 35%,
        rgba(230, 200, 70, 0.18) 60%,
        transparent 100%);
  }

  .emblem-plate {
    position: absolute;
    left: 0; bottom: 0;
    width: 100%;
    height: 166px;
  }

  .brand-name {
    position: absolute;
    left: 0; right: 0;
    text-align: center;
    color: var(--name-white);
    letter-spacing: 0.08em;
    font-size: 15px;
  }
  .product-line {
    position: absolute;
    left: 0; right: 0;
    text-align: center;
    letter-spacing: 0.04em;
  }

  .sleeve--front .brand-name   { top: 326px; }
  .sleeve--front .product-line { top: 350px; font-size: 12px; color: var(--accent-orange); }

  .name-tag {
    position: absolute;
    left: 12px; right: 12px;
    top: 42px;
    height: 66px;
    background: var(--label-grey);
  }
  .name-tag .brand-name   { top: 16px; font-size: 14px; }
  .name-tag .product-line { top: 38px; font-size: 9px; color: var(--accent-pink); letter-spacing: 0.12em; }

  .sleeve--back .brand-name   { top: 308px; }
  .sleeve--back .product-line { top: 348px; font-size: 9px; color: var(--accent-blue); letter-spacing: 0.14em; }

  .lid {
    position: absolute;
    left: 554px;
    top: 251px;
    width: 560px;
    height: 160px;
    overflow: hidden;
    background: var(--ink-black);
  }
  .lid .strand-field {
    background:
      linear-gradient(175deg,
        var(--strand-cyan) 0%, transparent 14%,
        var(--strand-magenta) 26%, transparent 38%,
        var(--strand-yellow) 50%, transparent 60%,
        var(--strand-green) 70%, transparent 82%,
        var(--strand-violet) 92%, transparent 100%),
      var(--ink-black);
  }
  .lid .name-tag {
    left: auto;
    right: 40px;
    top: 0;
    width: 76px;
    height: 64px;
  }
  .lid .name-tag .brand-name   { top: 14px; font-size: 13px; }
  .lid .name-tag .product-line { top: 36px; font-size: 8px; }
</style>
</head>
<body>
<main class="sheet">

  <section class="sleeve sleeve--front">
    <div class="strand-field" role="img" aria-label="Flowing colourful glass-like strands on black"></div>
    <svg class="emblem-plate" viewBox="0 0 136 166" aria-hidden="true">
      <polygon points="0,50 68,0 136,50 136,166 0,166" fill="#0b0b0c"/>
    </svg>
    <p class="brand-name">MELVOTA</p>
    <p class="product-line">GLASS PEN</p>
  </section>

  <section class="sleeve sleeve--side">
    <div class="strand-field" role="img" aria-label="Flowing colourful glass-like strands on black"></div>
    <div class="name-tag">
      <p class="brand-name">MELVOTA</p>
      <p class="product-line">GLASS PEN</p>
    </div>
  </section>

  <section class="sleeve sleeve--back">
    <div class="fountain-field" role="img" aria-label="Fine colourful strands fanning upward from a single point"></div>
    <p class="brand-name">MELVOTA</p>
    <p class="product-line">GLASS PEN</p>
  </section>

  <section class="lid">
    <div class="strand-field" role="img" aria-label="Flowing colourful glass-like strands across the black lid"></div>
    <div class="name-tag">
      <p class="brand-name">MELVOTA</p>
      <p class="product-line">GLASS PEN</p>
    </div>
  </section>

</main>
</body>
</html>
```